Coffee Roaster Needs A Postcard Design

I am coffee roaster ( a home business) and I would like to create a neighborhood delivery service. Once a month I would delivery fresh roasted coffee to my neighbors. I would like to create a postcard to advertise the coffee delivery service.

Preferences: The postcard would be very simple, primarily black and white ( a little color) with visuals; fresh roasted coffee beans, delivered to the doorstep, a great cup of coffee. Simple steps, 1 2 & 3.

I have a website the postcard advertisement should flow with the site : www.brinmoorcoffeeworks.com

Target Market(s)

Upper class residential neighborhood

Industry/Entity Type

Business

Font styles to use
Serif

Colors
f04a50

Requirements
Must have
• Images _ Coffee Beans

```html
<!DOCTYPE html>
<html lang="en">
<head>
<meta charset="utf-8">
<title>Brinmoor Coffee Works – Delivery Postcard</title>
<link rel="stylesheet" href="https://fonts.googleapis.com/css2?family=Jost:ital,wght@0,300;0,400;0,700;1,400&display=swap">
<style>
  :root {
    --paper: #ffffff;
    --ink: #1f1f1f;
    --title-ink: #474747;
    --icon-disc: #5a5858;
    --rule: #6b6b6b;
    --box-line: #cfcfcf;
    --bean-dark: #8a7868;
    --bean-mid: #b9aea4;
    --bean-light: #e4ddd6;
  }
  html, body {
    margin: 0;
    padding: 0;
    width: 1200px;
    height: 924px;
    overflow: hidden;
    background: var(--paper);
  }
  .postcard {
    position: relative;
    width: 1200px;
    height: 924px;
    background: var(--paper);
    font-family: "Jost", "Futura", sans-serif;
    color: var(--ink);
    overflow: hidden;
  }
  .bean-photo {
    position: absolute;
    top: 0;
    left: 400px;
    width: 800px;
    height: 330px;
    background:
      radial-gradient(ellipse 120px 80px at 260px 90px, var(--bean-dark), transparent 70%),
      radial-gradient(ellipse 110px 80px at 420px 80px, var(--bean-dark), transparent 70%),
      radial-gradient(ellipse 100px 70px at 380px 190px, var(--bean-mid), transparent 70%),
      radial-gradient(ellipse 110px 70px at 560px 60px, var(--bean-mid), transparent 70%),
      radial-gradient(ellipse 110px 70px at 700px 110px, var(--bean-mid), transparent 70%),
      linear-gradient(180deg, var(--bean-light), transparent);
    -webkit-mask-image: linear-gradient(180deg, #000 35%, transparent 95%), linear-gradient(90deg, transparent 0%, #000 25%);
    -webkit-mask-composite: source-in;
    mask-image: linear-gradient(180deg, #000 35%, transparent 95%), linear-gradient(90deg, transparent 0%, #000 25%);
    mask-composite: intersect;
    opacity: 0.85;
  }
  .brand-name {
    position: absolute;
    top: 52px;
    left: 64px;
    margin: 0;
    font-weight: 300;
    font-size: 57px;
    line-height: 68px;
    letter-spacing: 3px;
    color: var(--title-ink);
  }
  .steps {
    position: absolute;
    left: 105px;
    top: 322px;
    width: 106px;
  }
  .step-icon {
    position: absolute;
    left: 0;
    width: 106px;
    height: 106px;
  }
  .step-icon--beans { top: 0; }
  .step-icon--bike { top: 181px; }
  .step-icon--cup { top: 356px; }
  .step-sign {
    position: absolute;
    left: 0;
    width: 106px;
    text-align: center;
    font-weight: 300;
    font-size: 40px;
    color: var(--icon-disc);
    line-height: 40px;
  }
  .step-sign--plus { top: 124px; }
  .step-sign--equals { top: 302px; }
  .divider {
    position: absolute;
    left: 267px;
    top: 287px;
    width: 2px;
    height: 533px;
    background: var(--rule);
  }
  .message {
    position: absolute;
    left: 290px;
    width: 830px;
    top: 302px;
    text-align: center;
    font-size: 25.5px;
    line-height: 33px;
  }
  .message p { margin: 0; }
  .intro { margin-bottom: 22px !important; }
  .site-link { font-weight: 700; }
  .signup { margin-bottom: 30px !important; }
  .offer { font-style: italic; }
  .promo-code {
    display: inline-block;
    margin: 11px 0 32px;
    width: 185px;
    height: 58px;
    border: 1.5px solid var(--box-line);
    font-weight: 700;
    font-size: 34px;
    line-height: 58px;
    letter-spacing: 1px;
  }
</style>
</head>
<body>
<main class="postcard">
  <div class="bean-photo" role="img" aria-label="Soft-focus photo of roasted coffee beans on a wooden surface, fading to white"></div>

  <h1 class="brand-name">BRINMOOR<br>COFFEE<br>WORKS</h1>

  <div class="steps">
    <svg class="step-icon step-icon--beans" viewBox="0 0 106 106" aria-label="Coffee beans">
      <circle cx="53" cy="53" r="53" fill="var(--icon-disc)"/>
      <g fill="none" stroke="#fff" stroke-width="3">
        <ellipse cx="58" cy="36" rx="11" ry="7.5" transform="rotate(-30 58 36)"/>
        <path d="M50 40 Q58 34 66 32"/>
        <ellipse cx="42" cy="58" rx="11" ry="7.5" transform="rotate(-30 42 58)"/>
        <path d="M34 62 Q42 56 50 54"/>
        <ellipse cx="66" cy="68" rx="11" ry="7.5" transform="rotate(-30 66 68)"/>
        <path d="M58 72 Q66 66 74 64"/>
      </g>
    </svg>
    <div class="step-sign step-sign--plus">+</div>
    <svg class="step-icon step-icon--bike" viewBox="0 0 106 106" aria-label="Bicycle delivery">
      <circle cx="53" cy="53" r="53" fill="var(--icon-disc)"/>
      <g fill="none" stroke="#fff" stroke-width="2.5" stroke-linejoin="round" stroke-linecap="round">
        <circle cx="33" cy="60" r="12"/>
        <circle cx="73" cy="60" r="12"/>
        <path d="M33 60 L44 42 L64 42 L53 60 Z"/>
        <path d="M44 42 L41 36 M37 36 L46 36"/>
        <path d="M73 60 L62 36 L68 34"/>
      </g>
    </svg>
    <div class="step-sign step-sign--equals">=</div>
    <svg class="step-icon step-icon--cup" viewBox="0 0 106 106" aria-label="Cup of coffee">
      <circle cx="53" cy="53" r="53" fill="var(--icon-disc)"/>
      <g fill="#fff">
        <path d="M32 50 H70 V58 Q70 76 51 76 Q32 76 32 58 Z"/>
        <rect x="28" y="79" width="46" height="3" rx="1.5"/>
      </g>
      <path d="M70 54 Q80 54 78 62 Q76 68 68 68" fill="none" stroke="#fff" stroke-width="3"/>
      <path d="M47 44 Q43 38 47 32 Q51 26 47 20 M55 44 Q51 38 55 32 Q59 26 55 20" fill="none" stroke="#fff" stroke-width="1.5"/>
    </svg>
  </div>

  <div class="divider"></div>

  <section class="message">
    <p class="intro">We are a family-run coffee roasting business, in the Harlow Cove<br>
      neighborhood of Brinmoor, TX. If you enjoy a great cup of coffee,<br>
      we invite you subscribe to our monthly or semi-monthly coffee<br>
      delivery service. What could be better than fresh roasted<br>
      coffee beans delivered right to your door?</p>
    <p class="signup">Visit our website at <span class="site-link">www.brinmoorcoffeeworks.com</span> and<br>
      click on the Coffee Bean Subscriptions button at the top of the<br>
      page to sign up or learn more about us.</p>
    <p class="offer">New subscribers receive $2 off their first pound with the promo code:</p>
    <div class="promo-code">NEW10</div>
    <p class="closing">Support a local business and enjoy an excellent cup of coffee!</p>
  </section>
</main>
</body>
</html>
```